Award-winnning Estate Agent needs a premium version of their 'For Sale' board design

We need a premium option for our 'For Sale' board design. We have a standard board that is attached to this brief, but were are looking to have a premium design version that we will use when selling exclusive properties. Our company name is Harbour Lane Estates and the name for this is exclusive selection is: 'The Harbour Collection'. The design needs to work with our current brand, but have a distinctive PREMIUM feel to it. I have uploaded the barnd guidelines and also some of the exisisting logo variations. We do NOT need a new logo but feel free to play around with colours, fonts, sizes etc. for the sign.

Target Market(s)

Property buyers & house hunters

Industry/Entity Type

Real Estate - Residential Property

Font styles to use
Sans Serif

Requirements
Must have
• A premium fee, must be square design, must be easy to read when driving past the sign
Nice to have
• I'm open ot ideas

```html
<!DOCTYPE html>
<html lang="en">
<head>
<meta charset="utf-8">
<title>Harbour Lane Estates – For Sale Board</title>
<link rel="stylesheet" href="https://fonts.googleapis.com/css2?family=Archivo+Black&family=Arimo:wght@700&display=swap">
<style>
  :root {
    --navy: #2a3990;
    --sky: #29a8e0;
    --board: #ffffff;
    --page: #ffffff;
  }
  * { margin: 0; padding: 0; box-sizing: border-box; }
  html, body {
    width: 1200px;
    height: 621px;
    overflow: hidden;
    background: var(--page);
  }
  .canvas {
    position: relative;
    width: 1200px;
    height: 621px;
  }
  .sale-board {
    position: absolute;
    left: 320px;
    top: 30px;
    width: 560px;
    height: 560px;
    filter: drop-shadow(0 1px 3px rgba(0, 0, 0, 0.18));
  }
  .board-face { fill: var(--board); }
  .board-top-bar,
  .phone-band,
  .headline-rule { fill: var(--navy); }
  .brand-square { fill: var(--sky); }
  .brand-name {
    font-family: "Arimo", Arial, sans-serif;
    font-weight: 700;
    font-size: 48px;
    fill: var(--navy);
  }
  .headline {
    font-family: "Archivo Black", "Arial Black", sans-serif;
    font-size: 92px;
    fill: var(--navy);
  }
  .collection-name {
    font-family: "Arimo", Arial, sans-serif;
    font-weight: 700;
    font-size: 34px;
    fill: var(--navy);
  }
  .phone-number {
    font-family: "Archivo Black", "Arial Black", sans-serif;
    font-size: 70px;
    fill: var(--board);
  }
  .web-address {
    font-family: "Arimo", Arial, sans-serif;
    font-weight: 700;
    font-size: 33px;
    fill: var(--sky);
  }
</style>
</head>
<body>
  <main class="canvas">
    <svg class="sale-board" viewBox="0 0 560 560" xmlns="http://www.w3.org/2000/svg" aria-label="Harbour Lane Estates For Sale board">
      <rect class="board-face" x="0" y="0" width="560" height="560"/>
      <rect class="board-top-bar" x="0" y="0" width="560" height="15"/>

      <rect class="brand-square" x="240" y="52" width="80" height="80"/>
      <text class="brand-name" x="280" y="221" text-anchor="middle" textLength="397" lengthAdjust="spacingAndGlyphs">Harbour Lane Estates</text>

      <text class="headline" x="43" y="317" textLength="473" lengthAdjust="spacingAndGlyphs">FOR SALE</text>
      <rect class="headline-rule" x="43" y="335" width="475" height="3"/>
      <text class="collection-name" x="43" y="379" textLength="475" lengthAdjust="spacingAndGlyphs">THE HARBOUR COLLECTION</text>

      <rect class="phone-band" x="0" y="394" width="560" height="87"/>
      <text class="phone-number" x="43" y="462" textLength="473" lengthAdjust="spacingAndGlyphs">01632 960482</text>

      <text class="web-address" x="280" y="530" text-anchor="middle" textLength="459" lengthAdjust="spacingAndGlyphs">www.harbourlaneestates.co.uk</text>
    </svg>
  </main>
</body>
</html>
```